HM Quick Quote Screen

We are looking for two things:
1. On our main website (www.harborlinemutual.example) we would like to add a section for someone to enter their address and email address in return for a "quick quote."
2. Once they hit "enter" we would like a page built out that contains all the information that we would plug in from the backend.
We are an insurance company that focuses on property and powersports. This project in particular would focus on property (homeowner's specifically).
Reason: One of the decision makers will be out of the office until next week so we will provide our response next Tuesday. Thank you for your patience!
Insurance

```html
<!DOCTYPE html>
<html lang="en">
<head>
<meta charset="utf-8">
<title>Harborline Mutual — Home</title>
<link rel="stylesheet" href="https://fonts.googleapis.com/css2?family=Source+Sans+3:ital,wght@0,400;0,600;1,400&display=swap">
<style>
  :root {
    --brand-blue: #1b7ec4;
    --brand-deep: #0b55a5;
    --brand-bright: #1ea2e2;
    --top-bar: #1e8fcf;
    --ink: #4a4a4a;
    --muted: #777;
    --panel: #f4f5f6;
    --line: #d9dde0;
    --white: #ffffff;
    --contact-bg: #e9f4fb;
    --placeholder-light: #dde7ef;
    --placeholder-mid: #c3d2de;
  }
  * { box-sizing: border-box; margin: 0; padding: 0; }
  html, body { width: 960px; height: 1200px; overflow: hidden; }
  body {
    position: relative;
    background: var(--white);
    font-family: "Source Sans 3", "Myriad Pro", Arial, sans-serif;
    color: var(--ink);
  }
  .abs { position: absolute; }
  .top-bar { left: 0; top: 0; width: 960px; height: 6px; background: var(--top-bar); }
  .header-fade { left: 0; top: 140px; width: 960px; height: 318px; background: linear-gradient(#fff, #ececec); }

  .contact-strip {
    left: 536px; top: 8px; width: 422px; height: 38px;
    background: var(--contact-bg);
    color: var(--brand-blue); font-size: 14px;
    display: flex; align-items: center; justify-content: center; gap: 10px;
  }

  .brand { left: 28px; top: 72px; display: flex; align-items: center; gap: 10px; }
  .brand-mark { width: 22px; height: 22px; background: var(--brand-deep); }
  .brand-name { font-size: 27px; font-weight: 600; color: var(--brand-deep); letter-spacing: -0.3px; }

  .main-nav { left: 345px; top: 100px; height: 55px; display: flex; background: linear-gradient(#fbfbfb, #f0f0f0); }
  .main-nav a {
    display: flex; align-items: center; justify-content: center;
    height: 55px; font-size: 14px; color: var(--brand-blue); text-decoration: none;
    border-right: 1px solid var(--line);
  }
  .main-nav a.current { background: #e8e8e8; }
  .main-nav a.last { justify-content: flex-start; padding-left: 21px; border-right: 0; }

  .hero { left: 15px; top: 155px; width: 927px; height: 288px; border: 3px solid #c8dfee; }
  .hero-photo { left: 0; top: 0; width: 636px; height: 282px;
    background: linear-gradient(135deg, #2a62a6 0%, #6f9cc9 55%, #c9dcec 100%); }
  .hero-panel { left: 636px; top: 0; width: 285px; height: 282px;
    background: linear-gradient(160deg, var(--brand-deep) 0%, #1178c6 55%, var(--brand-bright) 100%);
    color: var(--white); padding: 19px 18px 0 19px; }
  .hero-title { font-size: 21px; font-weight: 600; line-height: 28px; }
  .hero-text { margin-top: 2px; font-size: 11px; line-height: 17px; }
  .hero-arrows { left: 28px; top: 193px; }
  .hero-actions { left: 15px; top: 226px; display: flex; align-items: center; gap: 6px; font-size: 13px; }
  .hero-actions a { background: #3a9bd9; color: var(--white); text-decoration: none; padding: 0 9px; height: 26px; line-height: 26px; display: block; }

  h2.section-title { font-size: 17px; font-weight: 400; color: var(--brand-blue); }
  .welcome { left: 28px; top: 480px; width: 622px; }
  .welcome p { margin-top: 7px; font-size: 11.4px; line-height: 17px; color: var(--ink); }
  .welcome p + p { margin-top: 17px; }

  .service { width: 280px; top: 737px; }
  .service-photo { width: 279px; height: 107px; margin-top: 15px; box-shadow: 0 6px 6px -4px rgba(0,0,0,.15);
    background: linear-gradient(160deg, var(--placeholder-light), var(--placeholder-mid)); }
  .service-lead { margin-top: 14px; font-size: 13px; line-height: 15px; color: var(--brand-blue); padding-left: 3px; }
  .service-text { margin-top: 15px; font-size: 11px; line-height: 15px; color: #2b86c9; padding-left: 3px; }
  .read-more { margin-top: 14px; border-top: 3px solid #d4e7f4; padding-top: 6px; font-size: 12.5px; color: var(--brand-deep); padding-left: 3px; }
  .divider { left: 327px; top: 745px; height: 300px; border-left: 1px dashed #bbb; }

  .quote-panel { left: 677px; top: 462px; width: 263px; height: 338px; background: linear-gradient(#f5f6f7, #fafafa); }
  .quote-panel h2 { position: absolute; left: 25px; top: 20px; font-size: 18px; }
  .field { position: absolute; left: 21px; width: 224px; height: 24px; border: 1px solid var(--line); border-radius: 8px;
    background: var(--white); font-size: 12px; color: var(--muted); padding: 4px 12px; }
  .field.area { left: 24px; width: 225px; height: 96px; }
  .submit { position: absolute; left: 29px; top: 269px; width: 70px; height: 22px; border-radius: 8px;
    background: var(--brand-blue); color: var(--white); font-size: 12px; text-align: center; line-height: 22px; }

  .testimonials { left: 686px; top: 802px; width: 260px; height: 184px; background: #f3f3f3; padding: 12px 17px; border-radius: 4px; }
  .testimonials p { margin-top: 6px; font-size: 11px; line-height: 17px; font-style: italic; color: #6d6d6d; }
  .testimonials .author { margin-top: 9px; text-align: right; font-style: normal; font-size: 12px; }

  .footer { left: 0; top: 1073px; width: 960px; height: 127px; background: var(--panel); }
  .footer-nav { left: 23px; top: 22px; font-size: 12px; color: var(--brand-blue); display: flex; gap: 11px; }
  .copyright { left: 23px; top: 62px; font-size: 12px; color: var(--muted); }
  .social { left: 761px; top: 17px; display: flex; align-items: center; gap: 3px; font-size: 14px; color: var(--muted); }
  .social .label { margin-right: 13px; }
  .social i { display: block; width: 18px; height: 18px; border-radius: 3px; background: var(--brand-bright); }
</style>
</head>
<body>
  <div class="abs header-fade"></div>
  <div class="abs top-bar"></div>

  <div class="abs contact-strip"><span>Customer Services &nbsp;(800) 555-0142</span><span>|</span><span>Claims: (800) 555-0187</span></div>

  <div class="abs brand"><span class="brand-mark"></span><span class="brand-name">Harborline Mutual</span></div>

  <nav class="abs main-nav">
    <a class="current" style="width:87px">Home</a>
    <a style="width:100px">About Us</a>
    <a style="width:134px">Producer Locator</a>
    <a style="width:131px">Producer Login</a>
    <a class="last" style="width:143px">Contact</a>
  </nav>

  <section class="abs hero">
    <div class="abs hero-photo" role="img" aria-label="Photo of a curling blue ocean wave breaking with white spray"></div>
    <div class="abs hero-panel">
      <h1 class="hero-title">Insurance Company<br>Services</h1>
      <p class="hero-text">Brightwave Web Studio is a web service company, offering a wide range of services which range from designing and development, that is covering almost all the fields in the best possible way.<br>To be the best we know what and how to present beautifully the working of the client's</p>
      <svg class="abs hero-arrows" width="18" height="10" viewBox="0 0 18 10"><path d="M7 1 L2 5 L7 9Z M11 1 L16 5 L11 9Z" fill="#fff"/></svg>
      <div class="abs hero-actions"><a>REGISTER NOW</a><span>|</span><a>MAKE A PAYMENT</a></div>
    </div>
  </section>

  <section class="abs welcome">
    <h2 class="section-title">Welcome to Our Website Mainpage</h2>
    <p>Brightwave Web Studio is a web service company, offering a wide range of services which range from designing and development, that is covering almost all the fields in the best possible way. To be the best we know what and how to present beautifully the working of the client's need and their advantages be highlighted. We act in accordance with the Industry certified processes to deliver the best to our clients all over the world. Over years we have built a strong reputation in providing website design and web development services.</p>
    <p>Thus, Wanna get ahead in the competition with other websites Brightwave Web Studio provide you with an attractive and most convincing website to enhance your marketing goals.<br>The only way to success is through the right path and that's what we provide you. None of the other companies has the result we do. So stick to the best that's how you will be the best don't opt for the second best. Our expertise does not limit itself to web development but also it includes Web Hosting, Search Engine Optimization, E-Commerce. We partner hundreds of organization to enhance their business, marketing and profit goals.</p>
  </section>

  <article class="abs service" style="left:28px">
    <h2 class="section-title" style="padding-left:2px">Insurance &nbsp;Services</h2>
    <div class="service-photo" role="img" aria-label="Photo placeholder: hand saving a coin in a piggy bank"></div>
    <p class="service-lead">Brightwave Web Studio provides you the Search Engine Optimization making your website search engine</p>
    <p class="service-text">So that the website can achieve top position and ranking in the Internet searches and thereby increasing the scope for the website to be found by customers.</p>
    <p class="read-more">READ MORE</p>
  </article>
  <div class="abs divider"></div>
  <article class="abs service" style="left:345px">
    <h2 class="section-title" style="padding-left:3px">Insurance &nbsp;Services</h2>
    <div class="service-photo" role="img" aria-label="Photo placeholder: business team gathered around a laptop"></div>
    <p class="service-lead">Brightwave Web Studio provides you the Search Engine Optimization making your website search engine</p>
    <p class="service-text">So that the website can achieve top position and ranking in the Internet searches and thereby increasing the scope for the website to be found by customers.</p>
    <p class="read-more">READ MORE</p>
  </article>

  <aside class="abs quote-panel">
    <h2 class="section-title">Quick Quote</h2>
    <div class="field" style="top:54px">type your name</div>
    <div class="field" style="top:90px">type your phone</div>
    <div class="field" style="top:126px">type your email address</div>
    <div class="field area" style="top:162px">type your address</div>
    <div class="submit">SUBMIT</div>
  </aside>

  <aside class="abs testimonials">
    <h2 class="section-title">Testimonials</h2>
    <p>Brightwave Web Studio provides you the Search Engine Optimization making your website search engine friendly. So that the website can achieve top position and ranking in the Internet searches and thereby increasing the scope for the website to be found by customers.</p>
    <p class="author">By AUOTHR NAME</p>
  </aside>

  <footer class="abs footer">
    <div class="abs footer-nav"><span>Main</span><span>|</span><span>About Us</span><span>|</span><span>Producer Locator</span><span>|</span><span>Producer Login</span><span>|</span><span>Contact</span></div>
    <div class="abs copyright">© 2012 Company Name &nbsp;| &nbsp; All right reserved</div>
    <div class="abs social"><span class="label">Get In Touch</span><i></i><i></i><i></i><i></i></div>
  </footer>
</body>
</html>
```